Business Card Design Project

Require a business card for a swing band called "Brass and Lantern". We are a 6 piece band that performs at events and corporate functions. Our music is great for dancing to or just providing a classy background atmosphere for people to enjoy. Final design should communicate professionalism and style with a hint of fun.

Sorry, just realised that it needs to be single sided only. Also, no rounded edges.

Industry/Entity Type

Events

Requirements
Must have
• Contact number: 0438 216 903
email address: brassandlantern@mailpost.example
Website details: www.brassandlantern.example

```html
<!DOCTYPE html>
<html lang="en">
<head>
<meta charset="utf-8">
<title>Brass and Lantern — Business Card</title>
<link href="https://fonts.googleapis.com/css2?family=Poiret+One&family=Quattrocento&display=swap" rel="stylesheet">
<style>
  :root {
    --page: #ffffff;
    --card: #000000;
    --ink: #ffffff;
    --art-glow: #8a8a8a;
    --art-mid: #3c3c3c;
    --art-edge: #000000;
  }
  * { margin: 0; padding: 0; box-sizing: border-box; }
  html, body {
    width: 1200px;
    height: 644px;
    overflow: hidden;
    background: var(--page);
  }
  .canvas {
    position: relative;
    width: 1200px;
    height: 644px;
    background: var(--page);
  }
  .business-card {
    position: absolute;
    left: 0;
    top: 26px;
    width: 942px;
    height: 550px;
    background: var(--card);
    color: var(--ink);
    font-family: "Quattrocento", Georgia, serif;
    overflow: hidden;
  }
  .band-name {
    position: absolute;
    left: 0;
    top: 0;
    width: 640px;
    height: 300px;
    font-family: "Poiret One", "Quattrocento", serif;
    font-weight: 400;
    color: var(--ink);
  }
  .band-name span { position: absolute; line-height: 1; white-space: nowrap; }
  .band-name__first {
    left: 44px;
    top: 36px;
    font-size: 118px;
    letter-spacing: -1px;
  }
  .band-name__joiner {
    left: 272px;
    top: 148px;
    font-size: 46px;
  }
  .band-name__last {
    left: 330px;
    top: 180px;
    font-size: 60px;
    text-transform: uppercase;
    letter-spacing: 1px;
  }
  .band-name__initial { position: static !important; font-size: 84px; }
  .contact-list {
    position: absolute;
    left: 47px;
    top: 358px;
    list-style: none;
    font-size: 28px;
    line-height: 36px;
    color: var(--ink);
  }
  .feature-art {
    position: absolute;
    left: 600px;
    top: 0;
    width: 342px;
    height: 550px;
  }
</style>
</head>
<body>
  <main class="canvas">
    <section class="business-card">
      <h1 class="band-name" aria-label="Brass and Lantern">
        <span class="band-name__first">Brass</span>
        <span class="band-name__joiner">and</span>
        <span class="band-name__last"><span class="band-name__initial">L</span>antern</span>
      </h1>

      <ul class="contact-list">
        <li class="contact-list__phone">0438 216 903</li>
        <li class="contact-list__web">www.brassandlantern.example</li>
        <li class="contact-list__email">brassandlantern@mailpost.example</li>
      </ul>

      <svg class="feature-art" viewBox="0 0 342 550" role="img"
           aria-label="White line illustration of a cocktail glass with straw and citrus slice beside an upright saxophone">
        <defs>
          <radialGradient id="featureArtGlow" cx="0.45" cy="0.6" r="0.6">
            <stop offset="0" stop-color="var(--art-glow)"/>
            <stop offset="0.5" stop-color="var(--art-mid)"/>
            <stop offset="1" stop-color="var(--art-edge)"/>
          </radialGradient>
        </defs>
        <rect x="0" y="0" width="342" height="550" fill="url(#featureArtGlow)"/>
      </svg>
    </section>
  </main>
</body>
</html>
```